Help create retail shipping website

We need a Squarespace design for our company Tandem Parcel. We are a retail shipping service that offers mailboxes, shipping, notary, and printing services. This store is similar to a QMT store, BoxVane, and Wendle Post. We would like to have help designing our website. I will provide our logo for the website. I would like our website to be professional, but be very inviting.

```html
<!DOCTYPE html>
<html lang="en">
<head>
<meta charset="utf-8">
<title>Tandem Parcel — Mailboxes, Shipping, Notary</title>
<link rel="stylesheet" href="https://fonts.googleapis.com/css2?family=Montserrat:wght@400;600;700;800&family=Roboto:wght@400;500;700&display=swap">
<style>
:root{
  --red:#f40f0f;
  --ink:#111111;
  --navy:#1e2735;
  --navy-deep:#161d29;
  --grey:#6f6f6f;
  --line:#d9d9d9;
  --white:#ffffff;
}
*{box-sizing:border-box;margin:0;padding:0}
html,body{width:1200px;height:4438px;overflow:hidden}
body{position:relative;background:var(--white);font-family:"Roboto",Arial,sans-serif;color:var(--ink)}
.abs{position:absolute}
.btn{position:absolute;display:flex;align-items:center;justify-content:center;background:var(--red);color:var(--white);font-family:"Roboto",Arial,sans-serif;font-weight:700;font-size:14px;text-decoration:none}
.btn.dark{background:var(--ink)}
.h2{position:absolute;left:0;width:1200px;text-align:center;font-family:"Montserrat",Arial,sans-serif;font-size:34px;font-weight:700;line-height:1}
.h2 .thin{font-weight:400}
.red{color:var(--red)}
.white{color:var(--white)}
.body-text{font-size:13px;line-height:23px;color:var(--grey)}
.photo{position:absolute}

/* header */
.site-header{position:absolute;left:0;top:0;width:1200px;height:86px;background:var(--white)}
.brand{position:absolute;display:flex;align-items:center;gap:10px}
.brand-square{width:18px;height:18px;background:var(--red)}
.brand-name{font-family:"Montserrat",Arial,sans-serif;font-weight:700;font-size:21px;color:var(--red);line-height:1}
.nav a{position:absolute;top:36px;font-size:14px;font-weight:500;color:var(--ink);text-decoration:none}
.find-store{position:absolute;left:885px;top:34px;font-size:14px;font-weight:500;color:var(--ink);text-decoration:underline}

/* hero */
.hero{position:absolute;left:0;top:86px;width:1200px;height:634px;background:linear-gradient(90deg,#1f2a3a 0%,#2b3442 40%,#6b6a5c 70%,#8a8b5a 100%)}
.hero-title{position:absolute;left:143px;top:305px;font-family:"Montserrat",Arial,sans-serif;font-weight:700;font-size:38px;color:var(--white)}
.hero-text{position:absolute;left:143px;top:364px;width:460px;font-size:15px;line-height:25px;color:var(--white)}

/* services */
.services{position:absolute;left:0;top:1403px;width:1200px;height:460px;background:linear-gradient(180deg,#1d2634,#232c3a)}
.service-card{position:absolute;top:1543px;width:213px;height:151px;background:var(--red)}
.service-card .frame{position:absolute;left:12px;top:12px;right:12px;bottom:12px;border:2px solid var(--white);border-radius:4px}
.service-card .art{position:absolute;left:40px;top:30px;right:40px;bottom:30px;border-radius:4px}
.service-name{position:absolute;top:1718px;width:213px;text-align:center;font-size:15px;font-weight:700;color:var(--white)}
.service-text{position:absolute;top:1746px;width:213px;text-align:center;font-size:12.5px;line-height:19px;color:#e6e6e6}

.label{position:absolute;font-size:16px;font-weight:700;color:var(--ink)}
.rule{position:absolute;height:1px;background:var(--line)}

.band-red{position:absolute;left:0;top:2941px;width:1200px;height:272px;background:linear-gradient(90deg,var(--red),#f52a22,var(--red))}
.band-text{position:absolute;left:200px;width:800px;text-align:center;font-size:13px;line-height:22px;color:var(--white)}
.band-navy{position:absolute;left:0;top:3822px;width:1200px;height:305px;background:linear-gradient(180deg,var(--navy-deep),var(--navy))}

.news-title{position:absolute;top:3596px;width:286px;text-align:center;font-size:15.5px;font-weight:500;line-height:22px}
.news-text{position:absolute;top:3651px;width:286px;text-align:center;font-size:12.5px;line-height:21px;color:var(--grey)}

/* footer */
.foot-h{position:absolute;top:4183px;font-size:16px;font-weight:500}
.foot-list{position:absolute;top:4226px;list-style:none;font-size:13px;line-height:25px;color:var(--grey)}
.social{position:absolute;top:4291px;width:30px;height:30px;border:1.5px solid var(--ink);border-radius:50%}
.copyright{position:absolute;top:4398px;left:0;width:1200px;text-align:center;font-size:12px;color:var(--grey)}
</style>
</head>
<body>

<header class="site-header">
  <div class="brand" style="left:90px;top:32px">
    <div class="brand-square"></div>
    <div class="brand-name">Tandem Parcel</div>
  </div>
  <nav class="nav">
    <a style="left:415px">Home</a>
    <a style="left:475px">About Us</a>
    <a style="left:556px">Our Services</a>
    <a style="left:656px">Locations</a>
    <a style="left:730px">Contact Us</a>
  </nav>
  <a class="find-store">Find Store</a>
  <a class="btn" style="left:978px;top:24px;width:136px;height:40px">Track Package</a>
</header>

<section class="hero" role="img" aria-label="Warehouse worker in a safety vest taping a parcel box"></section>
<h1 class="hero-title"><span class="red">TANDEM</span> PARCEL</h1>
<p class="hero-text">Lorem ipsum dolor sit amet, consectetur adipiscing elit, sed do tempor incididunt ut labore et dolore magna aliqua.</p>
<a class="btn" style="left:143px;top:444px;width:172px;height:52px">GET STARTED</a>

<!-- specialty -->
<div class="photo" role="img" aria-label="Woman taping a cardboard box in a packing warehouse" style="left:145px;top:809px;width:456px;height:491px;background:linear-gradient(135deg,#7d8aa0,#b9a287 60%,#d8c3a3)"></div>
<h2 class="abs" style="left:696px;top:898px;font-family:'Montserrat',Arial,sans-serif;font-size:32px;line-height:41px;font-weight:700">SPECIALTY SHIPPING<br><span class="red" style="font-weight:400">BY TANDEM PARCEL</span></h2>
<p class="abs body-text" style="left:696px;top:998px;width:365px">Lorem ipsum dolor sit amet, consectetur adipiscing elit, sed do eiusmod tempor incididunt ut labore et dolore magna ad minim veniam, quis nostrud aliqua.</p>
<p class="abs body-text" style="left:696px;top:1078px;width:365px">Ut enim&nbsp; exercitation ullamco laboris nisi ut aliquip ex ea commodo consequat.</p>
<a class="btn" style="left:696px;top:1162px;width:130px;height:41px">LEARN MORE</a>

<!-- services -->
<section class="services" role="img" aria-label="Dark warehouse shelving background"></section>
<h2 class="h2 white" style="top:1472px"><span class="red thin">OUR</span> SERVICES</h2>

<div class="service-card" style="left:145px"><div class="frame"></div><div class="art" role="img" aria-label="Red mailbox" style="background:linear-gradient(135deg,#f7f7f7,#c9c9c9)"></div></div>
<div class="service-card" style="left:377px"><div class="frame"></div><div class="art" role="img" aria-label="Cardboard shipping box" style="background:linear-gradient(135deg,#f2f2f2,#c8a276)"></div></div>
<div class="service-card" style="left:609px"><div class="frame"></div><div class="art" role="img" aria-label="Notary stamp" style="background:linear-gradient(135deg,#f2f2f2,#5b3a2b)"></div></div>
<div class="service-card" style="left:842px"><div class="frame"></div><div class="art" role="img" aria-label="Printed business cards" style="background:linear-gradient(135deg,#f5f5f5,#cfcfcf)"></div></div>

<div class="service-name" style="left:145px">Mailboxes</div>
<div class="service-name" style="left:377px">Shipping</div>
<div class="service-name" style="left:609px">Notary</div>
<div class="service-name" style="left:842px">Printing Services</div>
<p class="service-text" style="left:145px">Lorem ipsum dolor consectetur adipiscing elit, sed do</p>
<p class="service-text" style="left:377px">Lorem ipsum dolor consectetur adipiscing elit, sed do</p>
<p class="service-text" style="left:609px">Lorem ipsum dolor consectetur adipiscing elit, sed do</p>
<p class="service-text" style="left:842px">Lorem ipsum dolor consectetur adipiscing elit, sed do</p>

<!-- small business -->
<h2 class="h2" style="top:1951px">SMALL BUSINESS <span class="red thin">ESSENTIALS</span></h2>

<div class="label" style="left:143px;top:2035px">Single-use restaurant menus in hand</div>
<div class="photo" role="img" aria-label="Man working at a print shop machine" style="left:145px;top:2080px;width:456px;height:275px;background:linear-gradient(135deg,#d7dad9,#9a8c80 55%,#5d4a43)"></div>
<p class="abs body-text" style="left:143px;top:2380px;width:460px">Lorem ipsum dolor sit amet, consectetur adipiscing elit, sed do eiusmod tempor incididunt ut labore et dolore magna aliqua.</p>
<div class="rule" style="left:145px;top:2469px;width:456px"></div>

<div class="label" style="left:675px;top:2121px">Get Noticed with Large Printed Banners</div>
<div class="photo" role="img" aria-label="Hand pressing a red self-inking stamp onto paper" style="left:680px;top:2175px;width:375px;height:210px;background:linear-gradient(135deg,#5b5e63,#b9bcc0 60%,#e3e4e6)"></div>
<p class="abs body-text" style="left:680px;top:2409px;width:375px">Lorem ipsum dolor sit amet, consectetur adipiscing elit, sed tempor incididunt ut labore et dolore magna aliqua.</p>
<div class="rule" style="left:683px;top:2529px;width:370px"></div>

<div class="label" style="left:219px;top:2521px">Get Noticed with Large Printed Banners</div>
<div class="photo" role="img" aria-label="Container ship sailing at sunset" style="left:224px;top:2574px;width:375px;height:208px;background:linear-gradient(180deg,#c9a58a,#e7b98a 35%,#5f8095 60%,#2f5a78)"></div>
<p class="abs body-text" style="left:224px;top:2806px;width:375px">Lorem ipsum dolor sit amet, consectetur adipiscing elit, sed tempor incididunt ut labore et dolore magna aliqua.</p>

<p class="abs" style="left:683px;top:2654px;width:400px;font-size:14.5px;font-weight:500;text-align:center;margin-left:-20px">Stay inspired with helpful tips, stories, and news.</p>
<a class="btn" style="left:756px;top:2708px;width:253px;height:49px">PRESS &amp; SUCCESS STORIES</a>

<!-- certified -->
<section class="band-red" role="img" aria-label="Red tinted stack of parcels background"></section>
<h2 class="h2 white" style="top:2993px">CERTIFIED PACKING <span class="thin">EXPERTS</span></h2>
<p class="band-text" style="top:3043px">Lorem ipsum dolor sit amet, consectetur adipiscing elit, sed do eiusmod tempor incididunt ut labore et dolore magna aliqua. Ut quis nostrud exercitation ullamco laboris nisi ut aliquip ex ea commodo consequat.</p>
<a class="btn dark" style="left:497px;top:3113px;width:205px;height:43px">PACK AND SHIP TODAY</a>

<!-- news -->
<h2 class="h2" style="top:3302px"><span class="red thin">LATEST</span> NEWS</h2>

<div class="photo" role="img" aria-label="Person sealing a box with a tape dispenser" style="left:145px;top:3373px;width:285px;height:198px;background:linear-gradient(135deg,#6d5a4c,#d9c2a5 55%,#f1efec)"></div>
<div class="photo" role="img" aria-label="Product pouches with plants on a table" style="left:456px;top:3373px;width:286px;height:198px;background:linear-gradient(135deg,#6f7e62,#b39371 55%,#e6e1d8)"></div>
<div class="photo" role="img" aria-label="Warehouse aisle with stacked parcels" style="left:770px;top:3373px;width:285px;height:198px;background:linear-gradient(135deg,#2f6d72,#7c9c98 50%,#c28d5e)"></div>

<div class="news-title" style="left:145px">Lorem ipsum dolor sit consectetur adipiscing elit</div>
<div class="news-title" style="left:456px">Lorem ipsum dolor sit consectetur adipiscing elit</div>
<div class="news-title" style="left:770px">Lorem ipsum dolor sit consectetur adipiscing elit</div>
<p class="news-text" style="left:145px">Sed ut perspiciatis unde omnis iste natus error sit voluptatem accusantium</p>
<p class="news-text" style="left:456px">Sed ut perspiciatis unde omnis iste natus error sit voluptatem accusantium</p>
<p class="news-text" style="left:770px">Sed ut perspiciatis unde omnis iste natus error sit voluptatem accusantium</p>
<a class="btn" style="left:234px;top:3707px;width:107px;height:38px">Learn More</a>
<a class="btn" style="left:546px;top:3707px;width:107px;height:38px">Learn More</a>
<a class="btn" style="left:859px;top:3707px;width:107px;height:38px">Learn More</a>

<!-- estimate -->
<section class="band-navy" role="img" aria-label="Dark navy port with shipping containers background"></section>
<h2 class="h2 white" style="top:3891px"><span class="thin">ESTIMATE</span> SHIPPING COST</h2>
<p class="band-text" style="top:3942px">Lorem ipsum dolor sit amet, consectetur adipiscing elit, sed do eiusmod tempor incididunt ut labore et dolore magna aliqua. Ut quis nostrud exercitation ullamco laboris nisi ut aliquip ex ea commodo consequat.</p>
<a class="btn" style="left:497px;top:4012px;width:205px;height:43px">Estimate Shipping Cost</a>

<!-- footer -->
<footer>
  <div class="brand" style="left:145px;top:4240px">
    <div class="brand-square"></div>
    <div class="brand-name">Tandem Parcel</div>
  </div>
  <span class="social" style="left:229px" aria-label="Social link"></span>
  <span class="social" style="left:269px" aria-label="Social link"></span>
  <span class="social" style="left:307px" aria-label="Social link"></span>

  <div class="foot-h" style="left:506px">Links</div>
  <ul class="foot-list" style="left:506px"><li>Home</li><li>About Us</li><li>Our Services</li><li>Locations</li><li>Contact Us</li></ul>
  <div class="foot-h" style="left:658px">Links</div>
  <ul class="foot-list" style="left:658px"><li>Terms &amp; Condition</li><li>Privacy Policy</li><li>Support</li><li>Site Map</li><li>Find a Store</li></ul>
  <div class="foot-h" style="left:838px">Contact Us</div>
  <p class="abs" style="left:838px;top:4228px;width:230px;font-size:13px;line-height:21px;color:var(--grey)">Ferris Lane. 82 Ferris Ln, Harborview, HV 20417</p>
  <p class="abs" style="left:838px;top:4281px;font-size:13px;color:var(--grey)">info@tandemparcel.com</p>
  <p class="abs" style="left:838px;top:4316px;font-size:13px;color:var(--grey)">555-014-2290</p>
  <div class="rule" style="left:145px;top:4375px;width:910px"></div>
  <p class="copyright">© 2024&nbsp; Tandem Parcel&nbsp; |&nbsp; All Rights Reserved</p>
</footer>

</body>
</html>
```